Structural Engineering Business Card

Veltrow Drafts does residential house plans for clients in Central Florida. Would like simple but elegant business card that is appropriate for a house plan engineering company. Prefer black business card with black/white them but open to other shades of blue. I uploaded a sample card that I came across that looked good but please come up with your own creative designs.

Contact Information for Business Card

Name, Title, Phone, Email, Address, website

```html
<!DOCTYPE html>
<html lang="en">
<head>
<meta charset="UTF-8">
<title>Veltrow Drafts – Business Card</title>
<link rel="stylesheet" href="https://fonts.googleapis.com/css2?family=Oswald:wght@700&family=Open+Sans:wght@600&display=swap">
<style>
  :root {
    --ink: #16232e;
    --paper: #ffffff;
    --plan-light: #f1f1f1;
    --plan-mid: #d9d9d9;
    --label: #ffffff;
  }
  * { margin: 0; padding: 0; box-sizing: border-box; }
  html, body {
    width: 1200px;
    height: 750px;
    overflow: hidden;
    background: var(--paper);
  }
  .card {
    position: absolute;
    left: 74px;
    top: 74px;
    width: 1052px;
    height: 602px;
    background: var(--paper);
    border: 1px solid var(--ink);
    overflow: hidden;
  }
  .plan-backdrop {
    position: absolute;
    left: 0;
    top: 31px;
    width: 100%;
    height: 540px;
    background: linear-gradient(135deg, var(--plan-light) 0%, var(--paper) 45%, var(--plan-mid) 100%);
  }
  .frame-shapes {
    position: absolute;
    inset: 0;
  }
  .brand-panel {
    position: absolute;
    left: 213px;
    top: 186px;
    width: 625px;
    height: 204px;
    background: var(--ink);
    display: flex;
    align-items: center;
    justify-content: center;
    gap: 22px;
  }
  .brand-mark {
    width: 26px;
    height: 26px;
    background: var(--label);
  }
  .brand-name {
    font-family: "Oswald", sans-serif;
    font-weight: 700;
    font-size: 74px;
    letter-spacing: 1px;
    text-transform: uppercase;
    color: var(--label);
    line-height: 1;
  }
  .web-link {
    position: absolute;
    left: 766px;
    top: 547px;
    display: flex;
    align-items: center;
    gap: 16px;
    color: var(--label);
    font-family: "Open Sans", sans-serif;
    font-weight: 600;
    font-size: 16px;
  }
  .web-icon { width: 34px; height: 34px; }
</style>
</head>
<body>
  <main class="card">
    <div class="plan-backdrop" role="img" aria-label="Faint grey architectural floor plan drawing filling the card background"></div>

    <svg class="frame-shapes" width="1052" height="602" viewBox="0 0 1052 602" aria-hidden="true">
      <rect class="top-band" x="0" y="0" width="1052" height="31" fill="var(--ink)"/>
      <polygon class="top-tab" points="0,31 311,31 288,76 0,76" fill="var(--ink)"/>
      <rect class="bottom-band" x="0" y="571" width="1052" height="31" fill="var(--ink)"/>
      <polygon class="bottom-tab" points="761,526 1052,526 1052,571 741,571" fill="var(--ink)"/>
    </svg>

    <div class="brand-panel">
      <span class="brand-mark"></span>
      <h1 class="brand-name">Veltrow Drafts</h1>
    </div>

    <div class="web-link">
      <svg class="web-icon" viewBox="0 0 34 34" aria-hidden="true">
        <circle cx="17" cy="17" r="15" fill="var(--label)"/>
        <g fill="none" stroke="var(--ink)" stroke-width="2">
          <ellipse cx="17" cy="17" rx="6" ry="15"/>
          <line x1="2" y1="17" x2="32" y2="17"/>
          <line x1="5" y1="9" x2="29" y2="9"/>
          <line x1="5" y1="25" x2="29" y2="25"/>
        </g>
      </svg>
      <span class="web-address">www.yourwebsite.com</span>
    </div>
  </main>
</body>
</html>
```